Business card: GREEN HERONS TRADE SUPPLY

Hello,

This is your mission:

-I've just done my logo on the website. Now, I need A BUSINESS CARD.
-2 same business cards for 2 persons
-Landscape
-Dimension of the business card: 8.5 cm long and 5 cm high
-Different front and back
-For your information: this new company is selling products (fashion accessories, electronics, watches, fragrances, sunglasses, etc. to large clients related to shops in airlines (inflight catalogue), airports, cruises, etc.
-Colors and logo: please use the same colors of the logo attached (in blue with orange details) and follow the spirit of the existing logo.

-Front:
-1st person:
GREEN HERONS s.p.r.l.
Travel Retail Agency
www.greenheronsco.example
Lucien MARTOLIER
Partner
Mobile: +32480627315
Email: lm@greenheronsco.example
-2nd person:
GREEN HERONS s.p.r.l.
Travel Retail Agency
www.greenheronsco.example
Joris VANDERHOLME
Partner
Mobile: +32486153702
Email: jv@greenheronsco.example

-Back
Logo
see attached file. Please use the colors of the logo in blue with orange details.

Reason: I increase time necause i don t know if the deadline is in usa time or european time. I will make the selection at 9pm belgian time.

I'm selling products to large accounts/clients. Some of them do more than 2 Billion eur turnover

Airlines

Must have
• Use the logo.
The buyers get so many business cards.
They should remember me easily.
This is why my logo/company name is a stork and a color. 2 things that people usually remember easily.

```html
<!DOCTYPE html>
<html lang="en">
<head>
<meta charset="utf-8">
<title>Green Herons Trade Supply — Business Cards</title>
<link rel="stylesheet" href="https://fonts.googleapis.com/css2?family=Roboto:ital,wght@0,400;0,500;1,500&family=Roboto+Condensed:wght@400&display=swap">
<style>
  :root {
    --navy: #0b4a86;
    --band: #0d4784;
    --teal: #2a9bbf;
    --orange: #f08a24;
    --ink-label: #333333;
    --paper: #ffffff;
  }
  * { box-sizing: border-box; margin: 0; padding: 0; }
  html, body {
    width: 1150px; height: 1200px; overflow: hidden;
    background: var(--paper);
    font-family: "Roboto", Arial, sans-serif;
  }
  .sheet { position: relative; width: 1150px; height: 1200px; }

  .card-label {
    position: absolute; left: 25px;
    font: 500 18px "Roboto", Arial, sans-serif;
    color: var(--ink-label);
  }

  .card {
    position: absolute; left: 22px;
    width: 520px; height: 305px;
    background: var(--paper);
    border: 1px solid #222;
    overflow: hidden;
  }
  .card--front-1 { top: 47px; }
  .card--front-2 { top: 450px; }
  .card--back { top: 871px; left: 25px; }

  .wordmark {
    position: absolute; left: 28px; top: 76px; width: 240px;
    text-align: center; color: var(--navy);
    font-weight: 500; line-height: 1.05;
  }
  .wordmark__name { display: block; font-size: 25px; letter-spacing: 1px; }
  .wordmark__tag { display: block; font-size: 12px; letter-spacing: 4px; margin-top: 4px; }

  .scene-photo { position: absolute; left: 349px; top: -11px; width: 172px; height: 172px; }

  .contact {
    position: absolute; left: 114px; top: 128px; width: 290px;
    text-align: center; color: var(--navy);
    white-space: nowrap;
  }
  .contact__name { font-size: 17px; font-weight: 400; letter-spacing: -0.3px; }
  .contact__role { font-size: 12.5px; margin-top: 1px; }
  .contact__line { font-size: 13px; margin-top: 2px; }

  .rule { position: absolute; left: 0; width: 100%; height: 2px; }
  .rule--teal { top: 231px; background: var(--teal); }
  .rule--orange { top: 237px; background: var(--orange); }

  .band {
    position: absolute; left: 0; top: 241px; width: 100%; height: 64px;
    background: var(--band); color: var(--paper);
  }
  .band__company {
    position: absolute; left: 31px; top: 11px;
    font: 400 14px/1.1 "Roboto Condensed", "Arial Narrow", sans-serif;
  }
  .band__url {
    position: absolute; right: 32px; top: 24px;
    font: italic 500 15px "Roboto", Arial, sans-serif;
  }

  .wordmark--large {
    position: absolute; left: 0; top: 150px; width: 100%;
    text-align: center; color: var(--navy); font-weight: 500; line-height: 1.05;
  }
  .wordmark--large .wordmark__name { font-size: 50px; letter-spacing: 2px; }
  .wordmark--large .wordmark__tag { font-size: 23px; letter-spacing: 8px; margin-top: 8px; }
</style>
</head>
<body>
<main class="sheet">

  <p class="card-label" style="top:15px">Front 1</p>
  <section class="card card--front-1">
    <div class="wordmark">
      <span class="wordmark__name">GREEN HERONS</span>
      <span class="wordmark__tag">TRADE SUPPLY</span>
    </div>
    <svg class="scene-photo" viewBox="0 0 172 172" role="img" aria-label="Round photo of a tropical beach with palm trees under a blue sky">
      <defs>
        <linearGradient id="beach-1" x1="0" y1="0" x2="0" y2="1">
          <stop offset="0" stop-color="#6fb6e3"/>
          <stop offset="0.45" stop-color="#9fd3e6"/>
          <stop offset="0.6" stop-color="#4f8a3a"/>
          <stop offset="0.78" stop-color="#e9ecea"/>
          <stop offset="1" stop-color="#f4f4f1"/>
        </linearGradient>
      </defs>
      <circle cx="86" cy="86" r="86" fill="url(#beach-1)"/>
    </svg>
    <div class="contact">
      <p class="contact__name">Joris VANDERHOLME</p>
      <p class="contact__role">Partner</p>
      <p class="contact__line">Mob. +32486153702</p>
      <p class="contact__line">Email: jv@greenheronsco.example</p>
    </div>
    <div class="rule rule--teal"></div>
    <div class="rule rule--orange"></div>
    <div class="band">
      <p class="band__company">GREEN HERONS s.p.r.l.<br>Travel Retail</p>
      <p class="band__url">www.greenheronsco.example</p>
    </div>
  </section>

  <p class="card-label" style="top:418px">Front 2</p>
  <section class="card card--front-2">
    <div class="wordmark">
      <span class="wordmark__name">GREEN HERONS</span>
      <span class="wordmark__tag">TRADE SUPPLY</span>
    </div>
    <svg class="scene-photo" viewBox="0 0 172 172" role="img" aria-label="Round photo of a tropical beach with palm trees under a blue sky">
      <defs>
        <linearGradient id="beach-2" x1="0" y1="0" x2="0" y2="1">
          <stop offset="0" stop-color="#6fb6e3"/>
          <stop offset="0.45" stop-color="#9fd3e6"/>
          <stop offset="0.6" stop-color="#4f8a3a"/>
          <stop offset="0.78" stop-color="#e9ecea"/>
          <stop offset="1" stop-color="#f4f4f1"/>
        </linearGradient>
      </defs>
      <circle cx="86" cy="86" r="86" fill="url(#beach-2)"/>
    </svg>
    <div class="contact">
      <p class="contact__name">Lucien MARTOLIER</p>
      <p class="contact__role">Partner</p>
      <p class="contact__line">Mob. +32480627315</p>
      <p class="contact__line">Email: lm@greenheronsco.example</p>
    </div>
    <div class="rule rule--teal"></div>
    <div class="rule rule--orange"></div>
    <div class="band">
      <p class="band__company">GREEN HERONS s.p.r.l.<br>Travel Retail</p>
      <p class="band__url">www.greenheronsco.example</p>
    </div>
  </section>

  <p class="card-label" style="top:838px">Back</p>
  <section class="card card--back">
    <div class="wordmark--large">
      <span class="wordmark__name">GREEN HERONS</span>
      <span class="wordmark__tag">TRADE SUPPLY</span>
    </div>
  </section>

</main>
</body>
</html>
```